Willow Tri Fold Brochure
Tri Fold Brochure of Salon menu & services
Hello everyone, i have uploaded a few pics for the brochures.
are you prefer any size exactly for brochure ?
Inside sect 1 just design, sect 2 & 3 services, back sct 1 "front" lust design n comp name, back middle comp contact details, back sect 3 about us.
hi, will your brochure be a back to back trifold?..tnx..best regards

```html
<!DOCTYPE html>
<html lang="en">
<head>
<meta charset="utf-8">
<title>Willow Nail Spa – Tri Fold Brochure</title>
<link href="https://fonts.googleapis.com/css2?family=Open+Sans:wght@400;600;700&family=Great+Vibes&display=swap" rel="stylesheet">
<style>
  :root {
    --page-bg: #e8edf1;
    --sky: #1e9ad6;
    --sky-deep: #0c5f97;
    --navy: #0a3f6b;
    --ice: #d7f1fb;
    --pale: #f3fbff;
    --white: #ffffff;
    --ink: #123a57;
    --photo-violet: #5b4aa8;
    --photo-skin: #d9a88f;
  }
  * { box-sizing: border-box; margin: 0; padding: 0; }
  html, body { width: 1200px; height: 926px; overflow: hidden; }
  body {
    background: var(--page-bg);
    font-family: "Open Sans", Arial, sans-serif;
    color: var(--ink);
    position: relative;
  }
  .spread {
    position: absolute;
    top: 242px;
    width: 570px;
    height: 442px;
    background: linear-gradient(180deg, #3cb6ea 0%, var(--sky) 45%, var(--sky-deep) 100%);
    box-shadow: 0 6px 18px rgba(10,40,70,.25);
    overflow: hidden;
  }
  .spread--outside { left: 20px; }
  .spread--inside { left: 610px; }
  .panel {
    position: absolute; top: 0; width: 190px; height: 442px;
  }
  .panel + .panel { border-left: 1px solid rgba(255,255,255,.25); }
  .p1 { left: 0; } .p2 { left: 190px; } .p3 { left: 380px; }

  .band-title {
    position: absolute; left: 10px; right: 10px; height: 20px;
    background: linear-gradient(180deg, #ffffff 0%, var(--ice) 100%);
    border-radius: 3px;
    color: var(--sky-deep);
    font-weight: 700; font-size: 11px; letter-spacing: .5px;
    text-transform: uppercase; text-align: center; line-height: 20px;
  }
  .body-copy {
    position: absolute; left: 12px; right: 12px;
    color: var(--white); font-size: 7px; line-height: 1.5;
  }
  .photo { position: absolute; border: 2px solid var(--white); border-radius: 3px; }

  /* Outside spread */
  .about-photo {
    left: 10px; right: 10px; top: 186px; height: 246px;
    background: radial-gradient(circle at 40% 60%, #b59be0 0%, var(--photo-violet) 45%, #261d55 100%);
  }
  .contact-block { top: 34px; text-align: center; }
  .contact-block h4 { font-size: 7.5px; font-weight: 700; margin-top: 5px; }
  .hours-title { top: 168px; }
  .hours-table {
    position: absolute; left: 22px; right: 22px; top: 196px;
    border-collapse: collapse; color: var(--white); font-size: 8px;
  }
  .hours-table td { padding: 2px 0; border-bottom: 1px dotted rgba(255,255,255,.45); }
  .hours-table td:last-child { text-align: right; }
  .gift-note { top: 352px; text-align: center; font-style: italic; }

  .cover { background: var(--pale); }
  .cover-brand {
    position: absolute; top: 22px; left: 0; right: 0; text-align: center;
    font-weight: 700; color: var(--sky); font-size: 24px; letter-spacing: 1px;
  }
  .cover-brand small {
    display: block; font-size: 8px; letter-spacing: 4px; text-transform: uppercase; font-weight: 700;
  }
  .cover-photo {
    left: 0; right: 0; top: 82px; height: 170px; border: 0; border-radius: 0;
    background: linear-gradient(135deg, var(--photo-skin) 0%, #c08a78 40%, var(--photo-violet) 75%, #2e2670 100%);
  }
  .cover-wave {
    position: absolute; left: 0; top: 246px; width: 190px; height: 40px;
  }
  .cover-tagline {
    position: absolute; top: 300px; left: 0; right: 0; text-align: center;
    font-family: "Great Vibes", cursive; color: var(--sky); font-size: 22px; line-height: 1.1;
  }
  .cover-email {
    position: absolute; bottom: 12px; right: 12px; font-size: 7.5px; color: var(--sky-deep);
  }

  /* Inside spread */
  .women-photo {
    left: 10px; right: 10px; top: 10px; height: 110px;
    background: linear-gradient(135deg, #f1b8c9 0%, #d77fa5 50%, #8a5aa8 100%);
  }
  .services-title { top: 12px; left: 200px; right: 190px; position: absolute; }
  .services-intro { top: 38px; left: 200px; width: 180px; text-align: center; }
  .spa-photo {
    left: 390px; right: 10px; top: 10px; height: 110px;
    background: linear-gradient(135deg, #e3c39e 0%, #a8754f 55%, #5a3a26 100%);
  }
  .menu-box {
    position: absolute; width: 170px;
    background: rgba(255,255,255,.14);
    border: 1px solid rgba(255,255,255,.5);
    border-radius: 4px;
  }
  .menu-box h3 {
    background: linear-gradient(180deg, #fff 0%, var(--ice) 100%);
    color: var(--sky-deep); font-size: 8.5px; text-transform: uppercase;
    text-align: center; padding: 3px 0; border-radius: 3px 3px 0 0;
  }
  .menu-list { list-style: none; padding: 6px 10px; color: var(--white); font-size: 7.5px; line-height: 1.7; }
  .menu-list li { display: flex; justify-content: space-between; }
  .menu-photo { position: relative; height: 54px; margin: 5px 5px 0; border-radius: 2px; }
  .feet { background: linear-gradient(135deg, #f2d6c4, var(--photo-skin)); }
  .hands { background: linear-gradient(135deg, #f0d0c0, #b98470); }
  .wax { background: linear-gradient(135deg, #f4e1d0, #c99b7c); }
  .row-a { top: 132px; height: 112px; }
  .row-b { top: 256px; height: 156px; }
  .col-a { left: 10px; } .col-b { left: 200px; } .col-c { left: 390px; }
  .party-copy { color: var(--white); font-size: 8px; line-height: 1.6; text-align: center; padding: 10px 12px; }
  .package-note { top: 418px; left: 200px; width: 180px; text-align: center; font-size: 6.5px; }
</style>
</head>
<body>

<section class="spread spread--outside" aria-label="Outside of brochure">
  <div class="panel p1">
    <div class="band-title" style="top:10px">About Us</div>
    <p class="body-copy" style="top:38px">Willow Nail Spa is a calm place to rest, refresh and feel cared for. Our skilled team uses clean tools, gentle products and careful hands to give you lasting color and healthy nails. Walk in or book ahead, and let us make every visit a small escape from the busy day.</p>
    <div class="photo about-photo" role="img" aria-label="Close-up photo of manicured violet nails with sparkling glitter"></div>
  </div>

  <div class="panel p2">
    <div class="band-title" style="top:10px">Stay in touch!</div>
    <div class="body-copy contact-block">
      <h4>Mission Address</h4>
      <p>120 Kirumelano Ave, Suite 4<br>Brookfield, NV 80412</p>
      <h4>Mailing Address</h4>
      <p>PO Box 2210, Brookfield, NV 80412</p>
      <h4>Call Us</h4>
      <p>(555) 014-2286</p>
      <h4>E-mail Us</h4>
      <p>mrtoko@willowmail.com</p>
    </div>
    <div class="band-title hours-title">Our hours of operation</div>
    <table class="hours-table">
      <tr><td>Monday</td><td>9am – 7pm</td></tr>
      <tr><td>Tuesday</td><td>9am – 7pm</td></tr>
      <tr><td>Wednesday</td><td>9am – 7pm</td></tr>
      <tr><td>Thursday</td><td>9am – 8pm</td></tr>
      <tr><td>Friday</td><td>9am – 8pm</td></tr>
      <tr><td>Saturday</td><td>9am – 6pm</td></tr>
      <tr><td>Sunday</td><td>11am – 5pm</td></tr>
    </table>
    <p class="body-copy gift-note">Gift cards available for all services</p>
  </div>

  <div class="panel p3 cover">
    <div class="cover-brand">Willow<small>Nail Spa</small></div>
    <div class="photo cover-photo" role="img" aria-label="Photo of a hand with long violet polished nails"></div>
    <svg class="cover-wave" viewBox="0 0 190 40" aria-hidden="true">
      <path d="M0 10 C50 34 120 -4 190 18 L190 40 L0 40 Z" fill="#f3fbff"/>
      <path d="M0 14 C55 34 120 2 190 22" fill="none" stroke="#1e9ad6" stroke-width="2"/>
    </svg>
    <div class="cover-tagline">Rosalind's<br>Exclusive Nail Spa</div>
    <div class="cover-email">willowbrowbar@willowmail.com</div>
  </div>
</section>

<section class="spread spread--inside" aria-label="Inside of brochure">
  <div class="photo women-photo" role="img" aria-label="Photo of a group of smiling women at the salon"></div>
  <div class="band-title services-title">Our Services &amp; Products</div>
  <p class="body-copy services-intro">We carry a wide range of services, nail polish and products. Our team keeps tools clean and makes every visit relaxing. Please ask for our seasonal offers.</p>
  <div class="photo spa-photo" role="img" aria-label="Photo of the salon's pedicure chairs"></div>

  <div class="menu-box row-a col-a">
    <h3>Acrylic &amp; Gel Services</h3>
    <ul class="menu-list">
      <li><span>Full Set</span><span>$25</span></li>
      <li><span>Fill In</span><span>$15</span></li>
      <li><span>Pink &amp; White</span><span>$35</span></li>
      <li><span>Gel Full Set</span><span>$30</span></li>
    </ul>
  </div>
  <div class="menu-box row-a col-b">
    <h3>Private Parties</h3>
    <p class="party-copy">Call us for your next bachelorette party, ladies night out or princess party.</p>
  </div>
  <div class="menu-box row-a col-c">
    <h3>Other</h3>
    <ul class="menu-list">
      <li><span>Soak Off</span><span>$10</span></li>
      <li><span>Nail Art</span><span>$5</span></li>
      <li><span>Airbrush</span><span>$8</span></li>
      <li><span>Repair</span><span>$3</span></li>
      <li><span>Polish Change</span><span>$8</span></li>
    </ul>
  </div>

  <div class="menu-box row-b col-a">
    <h3>Pedicure</h3>
    <div class="menu-photo feet" role="img" aria-label="Photo of pampered feet during a pedicure"></div>
    <ul class="menu-list">
      <li><span>Classic Pedicure</span><span>$25</span></li>
      <li><span>Willow Pedicure</span><span>$35</span></li>
      <li><span>Gel Pedicure</span><span>$30</span></li>
      <li><span>Deluxe Pedicure</span><span>$45</span></li>
    </ul>
  </div>
  <div class="menu-box row-b col-b">
    <h3>Manicure</h3>
    <div class="menu-photo hands" role="img" aria-label="Photo of hands receiving a manicure"></div>
    <ul class="menu-list">
      <li><span>Classic Manicure</span><span>$15</span></li>
      <li><span>Willow Manicure</span><span>$25</span></li>
      <li><span>Gel Manicure</span><span>$25</span></li>
      <li><span>French Manicure</span><span>$20</span></li>
    </ul>
  </div>
  <div class="menu-box row-b col-c">
    <h3>Waxing</h3>
    <div class="menu-photo wax" role="img" aria-label="Photo of a waxing treatment"></div>
    <ul class="menu-list">
      <li><span>Eyebrow</span><span>$10</span></li>
      <li><span>Lip</span><span>$7</span></li>
      <li><span>Chin</span><span>$8</span></li>
      <li><span>Full Face</span><span>$30</span></li>
    </ul>
  </div>

  <p class="body-copy package-note">All package prices are upon request. All prices are quoted per individual group needs.</p>
</section>

</body>
</html>
```